Chiropody and Podiatry Flyer

A6 Flyer for a Chiropody Clinic.
Need to use an existing company logo (upload available).
Flyer should promote three aspects of the practice;
1) General chiropody : Nail Cutting; Corn Removal; Ingrown Nails; Hard Skin Removal; Verruca Treatment; Diabetic Assessment; Nail Surgery.
2) Home Visits - chiropody in the comfort of your own home.
3) Biomechanical Assessments / Orthotics
Colours should comprise navy blue/green/white to complement existing logo.
Promotional Offer on flyer.

Industry/Entity Type

Clinic

```html
<!DOCTYPE html>
<html lang="en">
<head>
<meta charset="utf-8">
<title>Stepwell Foot Clinic – Flyer</title>
<link rel="stylesheet" href="https://fonts.googleapis.com/css2?family=Arimo:wght@400;700&display=swap">
<style>
  :root {
    --navy: #30358f;
    --navy-deep: #1f2466;
    --green: #0aa84f;
    --green-light: #4cb848;
    --green-dark: #00913f;
    --lime: #a6ce39;
    --white: #ffffff;
    --page: #ffffff;
  }
  * { box-sizing: border-box; margin: 0; padding: 0; }
  html, body { width: 1200px; height: 1200px; overflow: hidden; background: var(--page); }
  body { position: relative; font-family: "Arimo", Arial, sans-serif; color: var(--white); }

  .flyer { position: absolute; top: 194px; width: 590px; height: 826px; overflow: hidden; }
  .flyer--back { left: 3px; background: var(--navy); }
  .flyer--front { left: 604px; background: radial-gradient(circle at 75% 20%, #5cc24a 0%, var(--green) 45%, var(--green-dark) 100%); }

  .flyer svg.shapes { position: absolute; inset: 0; width: 590px; height: 826px; }

  .art { position: absolute; }
  .art--leg-back { left: 0; top: 0; width: 300px; height: 690px;
    background: linear-gradient(160deg, rgba(255,255,255,0.04), rgba(255,255,255,0)); }
  .art--leg-front { left: 0; top: 300px; width: 380px; height: 526px;
    background: linear-gradient(200deg, rgba(255,255,255,0.04), rgba(255,255,255,0)); }
  .art--xray { left: 24px; top: 0; width: 180px; height: 198px; border-radius: 0 0 40px 40px;
    background: radial-gradient(ellipse at 35% 70%, #c8262c 0%, #6a1f55 35%, #1c2a6b 65%, rgba(20,30,80,0) 100%); }

  .treatment { position: absolute; width: 140px; height: 140px; border: 2px solid var(--white); border-radius: 50%;
    background: radial-gradient(circle, rgba(255,255,255,0.06), rgba(255,255,255,0)); }

  .brand { position: absolute; display: flex; align-items: center; gap: 10px; }
  .brand__mark { background: var(--white); flex: none; }
  .brand__name { font-weight: 400; color: var(--white); text-transform: uppercase; letter-spacing: 0.02em; }
  .flyer--back .brand { left: 189px; top: 44px; }
  .flyer--back .brand__mark { width: 44px; height: 44px; }
  .flyer--back .brand__name { font-size: 19px; line-height: 24px; }
  .flyer--front .brand { left: 253px; top: 42px; }
  .flyer--front .brand__mark { width: 60px; height: 60px; }
  .flyer--front .brand__name { font-size: 26px; line-height: 32px; }

  .contact { position: absolute; left: 0; right: 0; top: 680px; text-align: center; }
  .contact__title { font-weight: 700; font-size: 16px; line-height: 22px; }
  .contact__address { font-size: 15px; line-height: 22px; }
  .contact__lines { display: flex; justify-content: center; align-items: center; gap: 10px; margin-top: 22px; font-size: 16px; }
  .contact__icon { width: 24px; height: 24px; border-radius: 50%; background: var(--green-light); display: inline-flex; align-items: center; justify-content: center; }
  .contact__item { display: inline-flex; align-items: center; gap: 8px; }

  .service { position: absolute; left: 136px; width: 420px; display: flex; border-radius: 4px; overflow: hidden; background: var(--green-light); }
  .service__number { width: 60px; flex: none; background: var(--green); color: var(--navy); font-size: 48px; display: flex; align-items: center; justify-content: center; }
  .service__body { padding: 8px 10px 10px 19px; font-size: 19px; line-height: 25.5px; }
  .service__title { font-weight: 700; }
  .service--general { top: 280px; height: 144px; }
  .service--home { top: 436px; height: 88px; }
  .service--ortho { top: 538px; height: 64px; }
  .service--ortho .service__body { padding-top: 7px; }

  .badge { position: absolute; }
  .badge--partner { left: 324px; top: 634px; width: 110px; height: 80px; background: linear-gradient(180deg, #243c8c, #16204f); }
  .badge--register { left: 444px; top: 689px; width: 110px; height: 23px; background: var(--white); }
</style>
</head>
<body>

<section class="flyer flyer--back" aria-label="Flyer back: treatments and contact">
  <div class="art art--leg-back" role="img" aria-label="White line drawing of a leg and foot stepping forward"></div>

  <svg class="shapes" viewBox="0 0 590 826" aria-hidden="true">
    <path fill="var(--lime)" d="M0,622 C210,640 420,580 590,462 L590,478 C420,598 210,658 0,642 Z"/>
    <path fill="var(--green)" d="M0,646 C210,662 420,602 590,482 L590,826 L0,826 Z"/>
  </svg>

  <div class="brand">
    <span class="brand__mark"></span>
    <span class="brand__name">Stepwell<br>Foot<br>Clinic</span>
  </div>

  <div class="treatment" style="left:415px;top:69px" role="img" aria-label="Line drawing of hands massaging a foot"></div>
  <div class="treatment" style="left:275px;top:148px" role="img" aria-label="Line drawing of a toenail being trimmed"></div>
  <div class="treatment" style="left:415px;top:223px" role="img" aria-label="Line drawing of a sole with a verruca"></div>
  <div class="treatment" style="left:275px;top:298px" role="img" aria-label="Line drawing of two feet showing toes"></div>
  <div class="treatment" style="left:415px;top:373px" role="img" aria-label="Line drawing of foot bones and an orthotic"></div>
  <div class="treatment" style="left:275px;top:450px" role="img" aria-label="Line drawing of a foot top view"></div>

  <div class="contact">
    <p class="contact__title">Contact us</p>
    <p class="contact__address">Linden Court (1st Floor), 48 Harrow Yard<br>Elm Lane, London SE9 4QT</p>
    <p class="contact__lines">
      <span class="contact__item">
        <span class="contact__icon"><svg width="10" height="14" viewBox="0 0 10 14"><rect x="1" y="0.8" width="8" height="12.4" rx="1.5" fill="none" stroke="#fff" stroke-width="1.4"/></svg></span>
        +44 20 7946 0321
      </span>
      <span class="contact__item">
        <span class="contact__icon"><svg width="16" height="16" viewBox="0 0 16 16" fill="none" stroke="#fff" stroke-width="1.1"><circle cx="8" cy="8" r="6.5"/><ellipse cx="8" cy="8" rx="3" ry="6.5"/><path d="M1.5 8h13M2.5 4.8h11M2.5 11.2h11"/></svg></span>
        www.stepwellfoot.org
      </span>
    </p>
  </div>
</section>

<section class="flyer flyer--front" aria-label="Flyer front: services">
  <svg class="shapes" viewBox="0 0 590 826" aria-hidden="true">
    <path fill="var(--lime)" d="M0,352 C150,240 350,172 590,160 L590,176 C350,188 150,258 0,372 Z"/>
    <path fill="var(--navy)" d="M0,376 C150,262 350,192 590,180 L590,826 L0,826 Z"/>
    <path fill="var(--lime)" d="M120,826 C290,760 450,740 590,738 L590,754 C450,756 300,776 150,826 Z"/>
    <path fill="var(--green)" d="M150,826 C300,776 450,758 590,756 L590,826 Z"/>
  </svg>

  <div class="art art--xray" role="img" aria-label="X-ray style image of two lower legs with one ankle glowing red"></div>
  <div class="art art--leg-front" role="img" aria-label="White line drawing of a leg and foot stepping forward"></div>

  <div class="brand">
    <span class="brand__mark"></span>
    <span class="brand__name">Stepwell<br>Foot<br>Clinic</span>
  </div>

  <div class="service service--general">
    <span class="service__number">1</span>
    <div class="service__body">
      <p class="service__title">General Chiropody</p>
      <p>Nail Cutting, Corn Removal, Ingrown Nails, Hard Skin Removal, Verruca Treatment, Diabetic Assessment, Nail Surgery.</p>
    </div>
  </div>

  <div class="service service--home">
    <span class="service__number">2</span>
    <div class="service__body">
      <p class="service__title">Home Visits</p>
      <p>chiropody in the comfort of your own home.</p>
    </div>
  </div>

  <div class="service service--ortho">
    <span class="service__number">3</span>
    <div class="service__body">
      <p>Biomechanical Assessments / Orthotics</p>
    </div>
  </div>

  <div class="badge badge--partner"></div>
  <div class="badge badge--register"></div>
</section>

</body>
</html>
```